Business Card and Stationary
Small management consulting firm
Professional
Dwight Parmelee
President
5142 Heron Loop
Dunmore Crossing, VA 22817
dwight.parmelee@lw-advis.com
http://www.lw-advis.com
Our audience will be industry members of the defense consulting world as well as the US Government so we will need something memorable, but nothing too over the top.
Our Logo,
The slogan: "Real Strategy, Meaningful Change"
Our website: www.lw-advis.com
Here is the second design with our logo on the side

```html
<!DOCTYPE html>
<html lang="en">
<head>
<meta charset="utf-8">
<title>Lodgewood Advisory — Business Card</title>
<link href="https://fonts.googleapis.com/css2?family=Arimo:ital,wght@0,700;1,400&family=Tinos&display=swap" rel="stylesheet">
<style>
  :root {
    --backdrop: #e9e6e1;
    --card: #ffffff;
    --navy: #1b4f93;
    --navy-deep: #123a73;
    --navy-light: #3f78bf;
    --crimson: #b3161d;
    --crimson-dark: #7e0e12;
    --ink: #2a2a2a;
  }
  * { margin: 0; padding: 0; box-sizing: border-box; }
  html, body { width: 1200px; height: 780px; overflow: hidden; }
  body {
    background: var(--backdrop);
    display: flex;
    align-items: center;
    justify-content: center;
  }
  .business-card {
    position: relative;
    width: 1000px;
    height: 572px;
    background: var(--card);
    border-radius: 28px;
    overflow: hidden;
    box-shadow: 0 14px 34px rgba(0,0,0,0.18);
  }
  .header-band {
    position: absolute;
    inset: 0 0 auto 0;
    width: 1000px;
    height: 240px;
  }
  .holder {
    position: absolute;
    top: 30px;
    right: 46px;
    text-align: right;
    color: #fff;
    font-family: "Arimo", Arial, sans-serif;
  }
  .holder-name { font-weight: 700; font-size: 30px; letter-spacing: 0.2px; }
  .holder-title { font-style: italic; font-size: 21px; margin-top: 4px; }
  .brand {
    position: absolute;
    top: 205px;
    left: 40px;
    display: flex;
    align-items: center;
    gap: 18px;
  }
  .brand-dot {
    width: 80px;
    height: 80px;
    border-radius: 50%;
    background: var(--navy);
    flex: none;
  }
  .brand-name {
    font-family: "Tinos", "Times New Roman", serif;
    font-weight: 400;
    font-size: 40px;
    line-height: 1;
    color: var(--navy);
    white-space: nowrap;
  }
  .contact {
    position: absolute;
    left: 46px;
    top: 345px;
    font-family: "Tinos", "Times New Roman", serif;
    color: var(--ink);
    font-size: 22px;
    line-height: 1.2;
  }
  .address { font-style: normal; margin-bottom: 14px; }
  .contact-list { list-style: none; }
  .contact-list li { display: flex; align-items: center; gap: 12px; margin-bottom: 6px; }
  .contact-list svg { width: 20px; height: 20px; fill: var(--navy-light); flex: none; }
</style>
</head>
<body>
  <article class="business-card">
    <svg class="header-band" viewBox="0 0 1000 240" aria-hidden="true">
      <defs>
        <linearGradient id="bandBlue" x1="0" y1="0" x2="0" y2="1">
          <stop offset="0" stop-color="#3f78bf"/>
          <stop offset="1" stop-color="#123a73"/>
        </linearGradient>
        <linearGradient id="bandRed" x1="0" y1="0" x2="1" y2="0">
          <stop offset="0" stop-color="#7e0e12"/>
          <stop offset="0.5" stop-color="#b3161d"/>
          <stop offset="1" stop-color="#7e0e12"/>
        </linearGradient>
      </defs>
      <path d="M0 0 H1000 V112 C820 100 640 140 470 175 C300 210 130 205 0 175 Z" fill="url(#bandRed)"/>
      <path d="M0 0 H1000 V100 C820 92 640 124 470 158 C300 192 130 190 0 160 Z" fill="url(#bandBlue)"/>
    </svg>

    <header class="holder">
      <div class="holder-name">Dwight Parmelee</div>
      <div class="holder-title">President</div>
    </header>

    <div class="brand">
      <span class="brand-dot"></span>
      <div class="brand-name">Lodgewood Advisory, LLC</div>
    </div>

    <section class="contact">
      <address class="address">
        5142 Heron Loop<br>
        Dunmore Crossing, VA 22817
      </address>
      <ul class="contact-list">
        <li>
          <svg viewBox="0 0 24 24"><path d="M6.6 10.8a15.1 15.1 0 0 0 6.6 6.6l2.2-2.2a1 1 0 0 1 1-.25 11.4 11.4 0 0 0 3.6.57 1 1 0 0 1 1 1V20a1 1 0 0 1-1 1A17 17 0 0 1 3 4a1 1 0 0 1 1-1h3.5a1 1 0 0 1 1 1c0 1.25.2 2.45.57 3.57a1 1 0 0 1-.25 1z"/></svg>
          540-318-2264
        </li>
        <li>
          <svg viewBox="0 0 24 24"><path d="M7 1h10a2 2 0 0 1 2 2v18a2 2 0 0 1-2 2H7a2 2 0 0 1-2-2V3a2 2 0 0 1 2-2zm0 3v14h10V4zm5 15.5a1.2 1.2 0 1 0 0 2.4 1.2 1.2 0 0 0 0-2.4z"/></svg>
          540-772-9046
        </li>
        <li>
          <svg viewBox="0 0 24 24"><path d="M12 2a10 10 0 1 0 5 18.7l-1-1.7A8 8 0 1 1 20 12v1.2a1.8 1.8 0 0 1-3.6 0V7.5h-2v.9A5 5 0 1 0 15 16a3.8 3.8 0 0 0 7-2.8V12A10 10 0 0 0 12 2zm0 13a3 3 0 1 1 0-6 3 3 0 0 1 0 6z"/></svg>
          dwight.parmelee@lw-advis.com
        </li>
        <li>
          <svg viewBox="0 0 24 24"><path d="M12 2a10 10 0 1 0 0 20 10 10 0 0 0 0-20zm6.9 6h-3a15 15 0 0 0-1.3-3.9A8 8 0 0 1 18.9 8zM12 4c.8 1.1 1.5 2.5 1.9 4h-3.8c.4-1.5 1.1-2.9 1.9-4zM4.3 14a8 8 0 0 1 0-4h3.4a16 16 0 0 0 0 4zm.8 2h3a15 15 0 0 0 1.3 3.9A8 8 0 0 1 5.1 16zm3-8h-3a8 8 0 0 1 4.3-3.9A15 15 0 0 0 8.1 8zM12 20c-.8-1.1-1.5-2.5-1.9-4h3.8c-.4 1.5-1.1 2.9-1.9 4zm2.3-6H9.7a14 14 0 0 1 0-4h4.6a14 14 0 0 1 0 4zm.3 5.9A15 15 0 0 0 15.9 16h3a8 8 0 0 1-4.3 3.9zM16.3 14a16 16 0 0 0 0-4h3.4a8 8 0 0 1 0 4z"/></svg>
          www.lw-advis.com
        </li>
      </ul>
    </section>
  </article>
</body>
</html>
```